Jewellery Store Web design

We are looking at a redesign of an exclusive jewellery store. The idea of what we want is to display the type of jewellery we sell. Our main product range is white diamonds. We do not want people to buy online. This site will not display any prices but only display photos and the information about the store.
The client believes in the saying “A picture makes a thousand words” so this site needs to be more pictures – less words.
The website that the client loves is:
www.pelwickgems.com
The existing site can be found at:
http://www.lumarothevaults.com.au/
The site cannot be written in flash as the site must be viewable on Vexa/Talvo devices and will be implemented with our already designed CMS.
This project is only for the PSD file. We will code up the final submission ourselves.
Updates
Reason: We have some great designs and we have decided to gurrantee the project and for those who want a payment gurrantee to enter.
Target Market(s)
Young Couples, 30+
Industry/Entity Type
Store
Look and feel
Each slider illustrates characteristics of the customer's brand and the style your logo design should communicate.

```html
<!DOCTYPE html>
<html lang="en">
<head>
<meta charset="utf-8">
<title>Lumaro The Vaults</title>
<link rel="stylesheet" href="https://fonts.googleapis.com/css2?family=PT+Sans&family=Tinos&family=Ubuntu:wght@300&display=swap">
<style>
  :root {
    --page-light: #f2f3f4;
    --header-top: #e6e7e8;
    --ink: #1c1f22;
    --body-text: #2b2f33;
    --rule: #cfd2d5;
    --button: #2a3640;
    --footer: #111a21;
    --footer-rule: #2b353d;
    --footer-text: #dfe3e6;
    --social: #2a2f33;
  }
  * { margin: 0; padding: 0; box-sizing: border-box; }
  html, body { width: 1200px; height: 1195px; overflow: hidden; background: var(--page-light); }
  .page { position: relative; width: 1200px; height: 1195px; overflow: hidden; }

  .site-header {
    position: absolute; left: 0; top: 0; width: 1200px; height: 226px;
    background: linear-gradient(180deg, var(--header-top) 0%, #f4f5f5 60%, #eeeff0 100%);
    border-top: 6px solid #d7d9db;
  }
  .brand { position: absolute; left: 0; top: 46px; width: 1200px; text-align: center; color: var(--ink); font-family: "Tinos", serif; }
  .brand-name { font-size: 50px; letter-spacing: 1px; line-height: 56px; }
  .brand-sub { font-size: 16px; letter-spacing: 1px; margin-top: 4px; }

  .main-nav { position: absolute; left: 0; top: 172px; width: 1200px; height: 42px; }
  .main-nav a {
    position: absolute; top: 8px; font-family: "Tinos", serif; font-size: 20px;
    color: var(--ink); text-decoration: none; white-space: nowrap;
  }
  .main-nav a::after {
    content: ""; display: inline-block; margin-left: 9px; vertical-align: middle;
    border-left: 5px solid var(--ink); border-top: 4px solid transparent; border-bottom: 4px solid transparent;
  }
  .nav-divider { position: absolute; top: 2px; height: 40px; border-left: 2px dotted #9ea3a7; }

  .hero { position: absolute; left: 0; top: 226px; width: 1200px; height: 709px;
    background: linear-gradient(180deg, #f5f6f6 0%, #eef0f1 100%); }
  .hero-photo {
    position: absolute; left: 486px; top: 0; width: 714px; height: 709px;
    background: radial-gradient(ellipse 46% 58% at 52% 54%, #5b4c55 0%, #8d7c80 30%, #d9d2cf 62%, rgba(242,243,244,0) 100%);
  }
  .hero-title { position: absolute; left: 77px; top: 142px; font-family: "Ubuntu", sans-serif; font-weight: 300; color: var(--ink); }
  .hero-title .line-1 { display: block; font-size: 43px; line-height: 50px; }
  .hero-title .line-2 { display: block; font-size: 30px; line-height: 40px; margin-top: 2px; }
  .hero-rule { position: absolute; left: 77px; top: 251px; width: 474px; border-top: 1px solid var(--rule); }
  .hero-copy { position: absolute; left: 77px; top: 262px; width: 424px; font-family: "PT Sans", sans-serif; font-size: 13px; line-height: 23.4px; color: var(--body-text); }
  .hero-copy p + p { margin-top: 8px; }
  .view-button {
    position: absolute; left: 77px; top: 449px; width: 136px; height: 37px; border-radius: 5px;
    background: var(--button); color: #fff; font-family: "PT Sans", sans-serif; font-size: 14px;
    line-height: 37px; text-align: center; text-decoration: none;
  }
  .slide-dots { position: absolute; left: 80px; top: 518px; display: flex; gap: 3px; }
  .slide-dots span { width: 10px; height: 9px; background: #2f3a43; }

  .site-footer { position: absolute; left: 0; top: 916px; width: 1200px; height: 279px; }
  .footer-wave { position: absolute; left: 0; top: 0; }
  .footer-links { position: absolute; left: 56px; top: 64px; width: 558px; font-family: "Tinos", serif; font-size: 15px; }
  .footer-row { display: flex; height: 37.5px; align-items: center; border-bottom: 1px solid var(--footer-rule); }
  .footer-row:last-child { border-bottom: none; }
  .footer-row a { color: var(--footer-text); text-decoration: none; position: relative; padding-left: 14px; }
  .footer-row a::before {
    content: ""; position: absolute; left: 0; top: 5px;
    border-left: 4px solid var(--footer-text); border-top: 3.5px solid transparent; border-bottom: 3.5px solid transparent;
  }
  .col-1 { width: 170px; } .col-2 { width: 164px; }
  .social { position: absolute; left: 1001px; top: 44px; display: flex; gap: 5px; }
  .social span { width: 40px; height: 40px; border-radius: 50%; background: radial-gradient(circle at 50% 35%, #4a5055, var(--social) 70%); border: 1px solid #05090c; }
  .copyright { position: absolute; right: 63px; top: 218px; font-family: "Tinos", serif; font-size: 13px; color: var(--footer-text); word-spacing: 1px; }
</style>
</head>
<body>
<div class="page">
  <header class="site-header">
    <div class="brand">
      <div class="brand-name">LUMARO</div>
      <div class="brand-sub">THE VAULTS</div>
    </div>
    <nav class="main-nav">
      <a href="#" style="left:60px">Home</a>
      <span class="nav-divider" style="left:164px"></span>
      <a href="#" style="left:209px">About Us</a>
      <span class="nav-divider" style="left:343px"></span>
      <a href="#" style="left:386px">Collection</a>
      <span class="nav-divider" style="left:522px"></span>
      <a href="#" style="left:568px">Diamonds</a>
      <span class="nav-divider" style="left:710px"></span>
      <a href="#" style="left:751px">Friends</a>
      <span class="nav-divider" style="left:874px"></span>
      <a href="#" style="left:912px">Products</a>
      <span class="nav-divider" style="left:1047px"></span>
      <a href="#" style="left:1083px">Contact</a>
    </nav>
  </header>

  <section class="hero">
    <div class="hero-photo" role="img" aria-label="Photograph of a woman wearing layered pearl and gemstone necklaces, bracelets and rings"></div>
    <h1 class="hero-title">
      <span class="line-1">Perth Jewellers specialising</span>
      <span class="line-2">in gold, diamonds and pearls</span>
    </h1>
    <div class="hero-rule"></div>
    <div class="hero-copy">
      <p>Brightwell Studio is a web service company, offering a wide range of services which range from designaing and development, that is covering almost all the fields in the best possible way.</p>
      <p>To be the best we know what and how to present beautifully the working of the client's need and their advantages be highlighted. We act in accordance with the Industry certified processes to deliver the best to our clients all over the world.</p>
    </div>
    <a class="view-button" href="#">view collection &#8250;</a>
    <div class="slide-dots"><span></span><span></span><span></span><span></span></div>
  </section>

  <footer class="site-footer">
    <svg class="footer-wave" width="1200" height="279" viewBox="0 0 1200 279" aria-hidden="true">
      <path d="M0 19 C120 14 220 26 330 22 C450 17 520 10 620 15 C720 20 780 28 870 20 C960 12 1040 8 1200 14 L1200 279 L0 279 Z" fill="var(--footer)"/>
    </svg>
    <div class="footer-links">
      <div class="footer-row"><span class="col-1"><a href="#">Main page</a></span><span class="col-2"><a href="#">Collections</a></span><span><a href="#">Diamonds Jewellery</a></span></div>
      <div class="footer-row"><span class="col-1"><a href="#">About Company</a></span><span class="col-2"><a href="#">Diamonds</a></span><span><a href="#">Silver Jewellery</a></span></div>
      <div class="footer-row"><span class="col-1"><a href="#">Gallery</a></span><span class="col-2"><a href="#">Friends</a></span><span><a href="#">Gold</a></span></div>
      <div class="footer-row"><span class="col-1"><a href="#">Recent Blog</a></span><span class="col-2"><a href="#">Contact</a></span></div>
    </div>
    <div class="social" aria-label="Social links"><span></span><span></span><span></span></div>
    <p class="copyright">© 2012 Company Name &nbsp;|&nbsp; All right reserved</p>
  </footer>
</div>
</body>
</html>
```